Real estate agent : RT Estates

I have done the attached logo designed by your company .
My business card description as below:
Name : Daniel Brooks
Mobile: 0412583047
Email : danielb@rtestates-demo.net.au
Sales & Property Management

```html
<!DOCTYPE html>
<html lang="en">
<head>
<meta charset="utf-8">
<title>RT Estates – Business Card</title>
<link rel="stylesheet" href="https://fonts.googleapis.com/css2?family=Montserrat:wght@400;500;700&display=swap">
<style>
  :root {
    --backdrop: #c4c5c7;
    --card-dark: #1f1f20;
    --card-light: #ffffff;
    --ink: #111111;
    --ink-soft: #1c1c1c;
    --brand-on-dark: #0b0b0b;
    --paper: #ffffff;
  }
  * { box-sizing: border-box; margin: 0; padding: 0; }
  html, body {
    width: 1200px; height: 900px; overflow: hidden;
    background: var(--backdrop);
    font-family: "Montserrat", sans-serif;
  }
  .canvas { position: relative; width: 1200px; height: 900px; }

  .card {
    position: absolute; top: 117px;
    width: 382px; height: 669px;
    border-radius: 15px; overflow: hidden;
  }
  .card--back { left: 187px; background: var(--card-dark); }
  .card--front { left: 628px; background: var(--card-light); color: var(--ink); }

  /* back */
  .brand-mark {
    position: absolute; left: 0; right: 0;
    text-align: center; font-weight: 700; line-height: 1;
  }
  .card--back .brand-mark {
    top: 300px; font-size: 46px; letter-spacing: 3px; color: var(--brand-on-dark);
  }
  .tagline {
    position: absolute; left: 0; right: 0; top: 737px; top: 620px;
    display: flex; align-items: center; justify-content: space-between;
    color: var(--paper); font-size: 12.5px; font-weight: 500; letter-spacing: 1.1px;
  }
  .tagline .rule { width: 32px; height: 2px; background: var(--paper); }

  /* front */
  .card--front .brand-mark {
    top: 118px; font-size: 48px; letter-spacing: 3px; color: var(--ink);
  }
  .name-band {
    position: absolute; left: 0; right: 0; top: 295px; height: 80px;
    background: var(--ink); color: var(--paper); text-align: center;
  }
  .name-band .name { margin-top: 11px; font-size: 29px; font-weight: 700; letter-spacing: 0.5px; }
  .name-band .role { margin-top: 6px; font-size: 16px; font-weight: 500; letter-spacing: 1.2px; }

  .contact-icons {
    position: absolute; top: 414px; left: 0; right: 0;
    display: flex; justify-content: center; gap: 8px;
  }
  .contact-icons svg { width: 15px; height: 15px; fill: var(--ink); }
  .contact-list {
    position: absolute; top: 440px; left: 0; right: 0;
    text-align: center; font-size: 17.5px; line-height: 28.5px; color: var(--ink-soft);
  }
  .contact-list .phone { letter-spacing: 2.5px; }

  .location-pin { position: absolute; top: 576px; left: 181px; width: 19px; height: 24px; fill: var(--ink); }
  .address {
    position: absolute; top: 614px; left: 0; right: 0;
    display: flex; align-items: center; justify-content: space-between;
    font-size: 17.5px; letter-spacing: 0.6px; color: var(--ink-soft);
  }
  .address .rule { width: 30px; height: 3px; background: var(--ink); }
</style>
</head>
<body>
<main class="canvas">
  <section class="card card--back" aria-label="Card back">
    <div class="brand-mark">RT ESTATES</div>
    <div class="tagline"><span class="rule"></span><span>SALES &amp; PROPERTY MANAGEMENT</span><span class="rule"></span></div>
  </section>

  <section class="card card--front" aria-label="Card front">
    <div class="brand-mark">RT ESTATES</div>
    <div class="name-band">
      <p class="name">DANIEL BROOKS</p>
      <p class="role">REAL ESTATE AGENT</p>
    </div>
    <div class="contact-icons" aria-hidden="true">
      <svg viewBox="0 0 24 24"><path d="M6.6 10.8a15.1 15.1 0 0 0 6.6 6.6l2.2-2.2a1 1 0 0 1 1-.25 11.4 11.4 0 0 0 3.6.57 1 1 0 0 1 1 1V20a1 1 0 0 1-1 1A17 17 0 0 1 3 4a1 1 0 0 1 1-1h3.5a1 1 0 0 1 1 1c0 1.25.2 2.45.57 3.57a1 1 0 0 1-.25 1z"/></svg>
      <svg viewBox="0 0 24 24"><path d="M2 5h20v14H2z M2 5l10 8 10-8" fill="none" stroke="#111" stroke-width="0"/><path d="M2 6.5V19h20V6.5l-10 7.5z"/><path d="M2.8 5h18.4L12 11.9z"/></svg>
      <svg viewBox="0 0 24 24"><path d="M12 2a10 10 0 1 0 0 20 10 10 0 0 0 0-20zm6.9 6h-2.9a15 15 0 0 0-1.4-3.6A8 8 0 0 1 18.9 8zM12 4c.8 1.2 1.5 2.5 1.9 4h-3.8c.4-1.5 1.1-2.8 1.9-4zM4.3 14a8 8 0 0 1 0-4h3.3a16 16 0 0 0 0 4zm.8 2h2.9c.3 1.3.8 2.5 1.4 3.6A8 8 0 0 1 5.1 16zM8 8H5.1a8 8 0 0 1 4.3-3.6C8.8 5.5 8.3 6.7 8 8zm4 12c-.8-1.2-1.5-2.5-1.9-4h3.8c-.4 1.5-1.1 2.8-1.9 4zm2.3-6H9.7a14 14 0 0 1 0-4h4.6a14 14 0 0 1 0 4zm.3 5.6c.6-1.1 1.1-2.3 1.4-3.6h2.9a8 8 0 0 1-4.3 3.6zm1.8-5.6a16 16 0 0 0 0-4h3.3a8 8 0 0 1 0 4z"/></svg>
    </div>
    <div class="contact-list">
      <p class="phone">0412583047</p>
      <p class="email">danielb@rtestates-demo.net.au</p>
      <p class="web">www.rtestates-demo.net.au</p>
    </div>
    <svg class="location-pin" viewBox="0 0 24 30" aria-hidden="true"><path d="M12 0A10 10 0 0 0 2 10c0 7.5 10 20 10 20s10-12.5 10-20A10 10 0 0 0 12 0zm0 14a4 4 0 1 1 0-8 4 4 0 0 1 0 8z"/></svg>
    <div class="address"><span class="rule"></span><span>Riverbend, VIC, 3099</span><span class="rule"></span></div>
  </section>
</main>
</body>
</html>
```